Brennwald Metrics GmbH
Brennwald Metrics GmbH - Financial Services
Creative Brief
Professional
Lionel T Brennwald
Managing Director
Lindenweg 42 CH-6300 Zug Switzerland
U.S. Telephone 203.555.0186
lionel.brennwald@brennwaldmetrics-example.ch
brennwaldmetrics-example.ch
Wedsite will have partial moon crater stripped across the top. It might be interesting on the business card. Hard to tell if it will be too busy. JPG attached. Else simple is better. Note that address is broken after 19, and after Zug. It doesn't show on the confirmation. Kindly upload business cards and stationary, not just Business cards. It has to be a package

```html
<!DOCTYPE html>
<html lang="en">
<head>
<meta charset="utf-8">
<title>Brennwald Metrics GmbH – Envelope Stationery</title>
<link rel="stylesheet" href="https://fonts.googleapis.com/css2?family=Cinzel:wght@500&family=Lato:wght@400&display=swap">
<style>
  :root {
    --bg: #e9e6e1;
    --paper: #ffffff;
    --navy: #1d3a78;
    --navy-deep: #0f1f4f;
    --blue: #2f5bb0;
    --ink: #4a5266;
    --moon-light: #d9d9d6;
    --moon-mid: #a9aaa6;
    --moon-dark: #5f615e;
    --band-text: #ffffff;
  }
  * { margin: 0; padding: 0; box-sizing: border-box; }
  html, body { width: 1200px; height: 866px; overflow: hidden; background: var(--bg); }
  .stationery { position: relative; width: 1200px; height: 866px; }

  .envelope {
    position: absolute; left: 160px; width: 880px; height: 405px;
    background: var(--paper);
    box-shadow: 0 6px 18px rgba(0,0,0,0.18);
    overflow: hidden;
  }
  .envelope--front { top: 18px; }
  .envelope--back { top: 443px; }

  .envelope svg.art { position: absolute; inset: 0; width: 880px; height: 405px; }

  .brand {
    position: absolute; left: 32px; top: 30px;
    display: flex; align-items: center; gap: 10px;
  }
  .brand__square { width: 34px; height: 34px; background: var(--navy); }
  .brand__name {
    font-family: "Cinzel", serif; font-weight: 500;
    font-size: 22px; line-height: 1.05; letter-spacing: 1.5px;
    color: var(--navy);
  }

  .sender {
    position: absolute; left: 34px; top: 84px;
    font-family: "Lato", sans-serif; font-size: 7.5px; letter-spacing: 0.8px;
    text-transform: uppercase; color: var(--ink); line-height: 15px;
  }

  .band-text {
    position: absolute; left: 78px; top: 342px;
    color: var(--band-text); line-height: 15px;
  }
  .band-text__email {
    font-family: "Lato", sans-serif; font-size: 7.5px; letter-spacing: 0.8px; text-transform: uppercase;
  }
  .band-text__web { font-family: "Cinzel", serif; font-size: 10px; letter-spacing: 0.6px; }

  .flap-brand {
    position: absolute; left: 0; right: 0; top: 104px;
    display: flex; justify-content: center; align-items: center; gap: 6px;
  }
  .flap-brand__square { width: 14px; height: 14px; background: var(--paper); }
  .flap-brand__name {
    font-family: "Cinzel", serif; font-weight: 500; font-size: 10px; letter-spacing: 1px; color: var(--paper);
  }
</style>
</head>
<body>
<main class="stationery">

  <section class="envelope envelope--front" aria-label="Envelope front">
    <svg class="art" viewBox="0 0 880 405" aria-hidden="false">
      <defs>
        <linearGradient id="moonFade" x1="0" y1="0" x2="1" y2="0">
          <stop offset="0" stop-color="#ffffff" stop-opacity="1"/>
          <stop offset="0.35" stop-color="var(--moon-light)" stop-opacity="0.6"/>
          <stop offset="1" stop-color="var(--moon-mid)"/>
        </linearGradient>
        <linearGradient id="moonTopFade" x1="0" y1="0" x2="0" y2="1">
          <stop offset="0" stop-color="#ffffff" stop-opacity="0.75"/>
          <stop offset="0.5" stop-color="#ffffff" stop-opacity="0"/>
        </linearGradient>
        <linearGradient id="bandGrad" x1="0" y1="0" x2="1" y2="0">
          <stop offset="0" stop-color="var(--navy-deep)"/>
          <stop offset="0.45" stop-color="var(--blue)"/>
          <stop offset="1" stop-color="var(--navy)"/>
        </linearGradient>
      </defs>
      <g role="img" aria-label="Photograph of a grey cratered lunar surface fading into white">
        <rect x="300" y="0" width="580" height="340" fill="url(#moonFade)"/>
        <rect x="300" y="0" width="580" height="340" fill="url(#moonTopFade)"/>
      </g>
      <path d="M0 318 C 250 300, 560 276, 880 262 L880 405 L0 405 Z" fill="url(#bandGrad)"/>
      <path d="M0 318 C 250 300, 560 276, 880 262" fill="none" stroke="#ffffff" stroke-width="2" opacity="0.9"/>
      <path d="M0 330 C 260 312, 580 290, 880 280" fill="none" stroke="#ffffff" stroke-width="1" opacity="0.55"/>
      <path d="M0 342 C 300 320, 600 300, 880 296" fill="none" stroke="#8fb0ea" stroke-width="0.8" opacity="0.5"/>
    </svg>

    <div class="brand">
      <span class="brand__square"></span>
      <span class="brand__name">Brennwald<br>Metrics</span>
    </div>

    <address class="sender">
      Lindenweg 42<br>
      CH-6300 Zug Switzerland<br>
      T 203.555.0186<br>
      E lionel.brennwald@brennwaldmetrics-example.ch
    </address>

    <div class="band-text">
      <div class="band-text__email">E lionel.brennwald@brennwaldmetrics-example.ch</div>
      <div class="band-text__web">www.brennwaldmetrics-example.ch</div>
    </div>
  </section>

  <section class="envelope envelope--back" aria-label="Envelope back with flap">
    <svg class="art" viewBox="0 0 880 405">
      <defs>
        <linearGradient id="flapGrad" x1="0" y1="0" x2="1" y2="0">
          <stop offset="0" stop-color="var(--blue)"/>
          <stop offset="0.4" stop-color="var(--navy-deep)"/>
          <stop offset="0.62" stop-color="var(--navy)"/>
          <stop offset="1" stop-color="var(--moon-dark)"/>
        </linearGradient>
        <linearGradient id="flapMoon" x1="0" y1="0" x2="1" y2="0">
          <stop offset="0" stop-color="var(--moon-mid)" stop-opacity="0"/>
          <stop offset="1" stop-color="var(--moon-mid)" stop-opacity="0.7"/>
        </linearGradient>
      </defs>
      <path d="M0 0 H880 V18 L820 138 H60 L0 18 Z" fill="url(#flapGrad)"/>
      <path d="M520 0 H880 V18 L820 138 H520 Z" fill="url(#flapMoon)" role="img" aria-label="Lunar surface photograph blending into the blue flap"/>
      <path d="M0 18 L60 138 H820 L880 18" fill="none" stroke="#c9ccd3" stroke-width="1"/>
    </svg>
    <div class="flap-brand">
      <span class="flap-brand__square"></span>
      <span class="flap-brand__name">Brennwald Metrics</span>
    </div>
  </section>

</main>
</body>
</html>
```